Velmar Ops Business Cards

We need to design some upbeat business cards. We are an Industrial Rope Access Company/Height Safety Company that specialize in Rope Access, Confined Space, Anchor Points, Safety Systems, PPE Inspecions and Rigging.
Company name is Velmar Ops Ltd
Card is for Gareth Lomas the Company Director
His mobile number is 027 418 9072 and email is gareth@velmarops.co.nz. Website address is www.velmarops.co.nz.
We will post some pictures below to ensure you get a good idea of what we do.

```html
<!DOCTYPE html>
<html lang="en">
<head>
<meta charset="utf-8">
<title>Velmar Ops – Business Cards</title>
<link rel="stylesheet" href="https://fonts.googleapis.com/css2?family=Exo+2:ital,wght@0,300;0,700;1,600;1,700&family=Michroma&family=Orbitron:wght@500&display=swap">
<style>
  :root {
    --navy: #1b174e;
    --white: #ffffff;
    --tagline: #c9c8dc;
    --page: #ffffff;
  }
  * { margin: 0; padding: 0; box-sizing: border-box; }
  html, body {
    width: 1200px; height: 1200px; overflow: hidden;
    background: var(--page);
  }
  .canvas { position: relative; width: 1200px; height: 1200px; }

  .card {
    position: absolute;
    width: 840px; height: 480px;
    background: var(--navy);
    border-radius: 38px;
    overflow: hidden;
    color: var(--white);
  }
  .card--front { left: 58px; top: 86px; }
  .card--back  { left: 302px; top: 628px; }

  /* Front */
  .brand {
    position: absolute; left: 0; width: 100%; top: 66px;
    text-align: center;
    font-family: "Exo 2", sans-serif; font-weight: 700;
    font-size: 70px; line-height: 1; letter-spacing: 1px;
  }
  .tagline {
    position: absolute; left: 0; width: 100%; top: 146px;
    text-align: center;
    font-family: "Exo 2", sans-serif; font-weight: 300;
    font-size: 21px; letter-spacing: 2px; color: var(--tagline);
  }
  .tagline .sep { margin: 0 12px; }
  .person {
    position: absolute; left: 0; width: 100%; top: 312px;
    text-align: center;
    font-family: "Michroma", sans-serif;
  }
  .person__name {
    font-size: 38px; line-height: 1; letter-spacing: 3px;
    font-variant: small-caps; text-transform: lowercase;
  }
  .person__name::first-letter { text-transform: uppercase; }
  .person__name .cap { text-transform: uppercase; }
  .person__role {
    margin-top: 12px;
    font-size: 24px; line-height: 1; letter-spacing: 3px;
    font-variant: small-caps;
  }
  .person__phone {
    margin-top: 16px;
    display: flex; justify-content: center; align-items: center; gap: 14px;
    font-family: "Orbitron", sans-serif; font-weight: 500;
    font-size: 26px; letter-spacing: 4px;
  }
  .person__phone svg { width: 24px; height: 24px; }

  /* Back */
  .crescent { position: absolute; left: 0; top: 0; width: 840px; height: 480px; }
  .rope { position: absolute; left: 0; top: 268px; width: 480px; height: 12px; }
  .contact {
    position: absolute; left: 44px; top: 190px;
    font-family: "Exo 2", sans-serif; font-style: italic; font-weight: 600;
    font-size: 25px; line-height: 34px;
  }
  .contact__row { display: flex; align-items: center; gap: 16px; }
  .contact__row svg { width: 26px; height: 26px; flex: none; }

  .services__title {
    position: absolute; left: 472px; top: 28px;
    font-family: "Exo 2", sans-serif; font-style: italic; font-weight: 700;
    font-size: 32px; letter-spacing: 0.5px;
  }
  .services__item {
    position: absolute;
    font-family: "Exo 2", sans-serif; font-style: italic; font-weight: 700;
    font-size: 24px; line-height: 1; letter-spacing: 0.5px;
    transform: translateY(-50%);
  }
  .services__item::before { content: "·"; margin-right: 6px; font-weight: 700; }
</style>
</head>
<body>
<div class="canvas">

  <section class="card card--front">
    <div class="brand">Velmar Ops</div>
    <div class="tagline">Safety<span class="sep">|</span>Integrity<span class="sep">|</span>Quality<span class="sep">|</span>Assurance</div>
    <div class="person">
      <div class="person__name">Gareth Lomas</div>
      <div class="person__role">Director</div>
      <div class="person__phone">
        <svg viewBox="0 0 24 24" aria-hidden="true"><path fill="#fff" d="M6.6 2.2l3 3.6c.5.6.4 1.4-.1 1.9L8 9.2c1.1 2.7 3.9 5.5 6.8 6.8l1.5-1.5c.5-.5 1.3-.6 1.9-.1l3.6 3c.6.5.7 1.4.2 2l-1.7 2c-.6.7-1.5 1-2.4.8C9.6 20.4 3.6 14.4 1.8 6.1c-.2-.9.1-1.8.8-2.4l2-1.7c.6-.5 1.5-.4 2 .2z"/></svg>
        <span>027 418 9072</span>
      </div>
    </div>
  </section>

  <section class="card card--back">
    <svg class="crescent" viewBox="0 0 840 480" aria-hidden="true">
      <path fill="#fff" d="M376 0 Q657 240 374 480 L366 480 Q588 240 368 0 Z"/>
    </svg>

    <div class="contact">
      <div class="contact__row">
        <svg viewBox="0 0 24 24" aria-hidden="true"><path fill="#fff" d="M23 1L1 10l8 3 1 9 4-6 5 4z"/></svg>
        <span>gareth@velmarops.co.nz</span>
      </div>
      <div class="contact__row">
        <svg viewBox="0 0 24 24" aria-hidden="true" fill="none" stroke="#fff" stroke-width="1.8"><circle cx="12" cy="12" r="10"/><ellipse cx="12" cy="12" rx="4.5" ry="10"/><path d="M2 12h20M4 6.5h16M4 17.5h16M12 2v20"/></svg>
        <span>www.velmarops.co.nz</span>
      </div>
    </div>

    <svg class="rope" viewBox="0 0 480 12" role="img" aria-label="Rope with a loop running across the card">
      <rect x="0" y="1" width="480" height="10" fill="#fff"/>
    </svg>

    <h2 class="services__title">We Specialize in :</h2>
    <div class="services__item" style="left:520px; top:110px;">Rope Access</div>
    <div class="services__item" style="left:542px; top:161px;">Confined Space</div>
    <div class="services__item" style="left:554px; top:212px;">Safety Systems</div>
    <div class="services__item" style="left:554px; top:265px;">PPE Certification</div>
    <div class="services__item" style="left:544px; top:316px;">Anchor Points</div>
    <div class="services__item" style="left:524px; top:366px;">Rigging</div>
  </section>

</div>
</body>
</html>
```